LBH Letterhead

I need letterhead for "lakeside birch holdings llc" ...

logo attached to project..

Company Info:
482 East Marlow Avenue, Suite 7B
Chicago, Illinois 60917
ofc 312-555-0148
facsimile 312-555-0193
www.lakesidebirchholdingsllc.example
info@lakesidebirchholdingsllc.example

I have multiple projects listed.. see below:

Business cards for lakeside birch holdings llc
letterhead "
envelopes "

Business cards for KV Commerce LLC
letterhead "
envelopes "

```html
<!DOCTYPE html>
<html lang="en">
<head>
<meta charset="utf-8">
<title>LBH Letterhead</title>
<link rel="stylesheet" href="https://fonts.googleapis.com/css2?family=Roboto+Condensed:wght@400&display=swap">
<style>
  :root {
    --stage: #5a5a5c;
    --stage-edge: #6a6a6c;
    --paper: #ffffff;
    --brand-navy: #15426f;
    --footer-text: #ffffff;
  }
  * { margin: 0; padding: 0; box-sizing: border-box; }
  html, body {
    width: 1200px;
    height: 1000px;
    overflow: hidden;
    background: var(--stage);
    font-family: "Roboto Condensed", "Arial Narrow", sans-serif;
  }
  .stage {
    position: absolute;
    left: 8px; top: 8px;
    width: 1184px; height: 984px;
    border: 1px solid var(--stage-edge);
  }
  .letterhead {
    position: absolute;
    left: 294px; top: 84px;
    width: 602px; height: 846px;
    background: var(--paper);
  }
  .brand {
    position: absolute;
    right: 34px; top: 86px;
    display: flex;
    flex-direction: column;
    align-items: flex-end;
    color: var(--brand-navy);
  }
  .brand-row {
    display: flex;
    align-items: center;
    gap: 8px;
  }
  .brand-mark {
    width: 14px; height: 14px;
    border-radius: 50%;
    background: var(--brand-navy);
  }
  .brand-name {
    font-size: 17px;
    letter-spacing: 0.5px;
    line-height: 1;
  }
  .brand-web {
    margin-top: 5px;
    font-size: 11px;
    letter-spacing: 1.6px;
    line-height: 1;
  }
  .letter-footer {
    position: absolute;
    left: 0; bottom: 0;
    width: 100%; height: 61px;
    background: var(--brand-navy);
    color: var(--footer-text);
    text-align: center;
    font-size: 11px;
    line-height: 14px;
    padding-top: 13px;
  }
</style>
</head>
<body>
  <div class="stage"></div>
  <main class="letterhead">
    <header class="brand">
      <div class="brand-row">
        <span class="brand-mark"></span>
        <span class="brand-name">Lakeside Birch Holdings LLC</span>
      </div>
      <span class="brand-web">www.lakesidebirchholdingsllc.example</span>
    </header>
    <footer class="letter-footer">
      <p class="footer-address">482 East Marlow Avenue, Suite 7B Chicago, Illinois 60917</p>
      <p class="footer-contact">Office: 312-555-0148 | Facsimile: 312-555-0193 | Email: info@lakesidebirchholdingsllc.example</p>
    </footer>
  </main>
</body>
</html>
```